Business Card for Graphic Design Firm

This project is for a new graphic design firm based in New Jersey called Velmoth. We outsource graphic design and marketing jobs. We want to communicate that this is a professional company but it as well creative and artistic. This card may be used as a horizontal double sided paper card or a vertical single sided translucent card so feel free to submit designs in whichever format or both.
Updates

Reason: Extending the deadline because I'm not exactly satisfied with the designs so far.

Please view the updated project brief

Target Market(s)

Adults aged 25-60

Industry/Entity Type

Graphic Design

Font styles to use
Serif
Sans Serif

Requirements
Nice to have
• Maybe a triangular pattern around the edges similar to our logo

```html
<!DOCTYPE html>
<html lang="en">
<head>
<meta charset="utf-8">
<title>Velmoth Business Card</title>
<link rel="stylesheet" href="https://fonts.googleapis.com/css2?family=Montserrat:wght@400;500&amp;family=Arimo:wght@400&amp;display=swap">
<style>
  :root {
    --backdrop: #c9cbcc;
    --card-slate: #5d666c;
    --wordmark-muted: #7d868c;
    --text-light: #e9ecee;
    --band-sky: #7cc3e6;
    --band-gold: #e0b21f;
    --band-orange: #e6952e;
  }
  * { margin: 0; padding: 0; box-sizing: border-box; }
  html, body { width: 1200px; height: 1000px; overflow: hidden; }
  body {
    background: var(--backdrop);
    font-family: "Arimo", Arial, sans-serif;
    position: relative;
  }
  .card {
    position: absolute;
    left: 280px;
    width: 640px;
    height: 366px;
    background: var(--card-slate);
    overflow: hidden;
  }
  .card--back { top: 64px; }
  .card--front { top: 500px; }

  .back-wordmark {
    position: absolute;
    left: 0; right: 0; top: 150px;
    text-align: center;
    font-family: "Montserrat", sans-serif;
    font-weight: 500;
    font-size: 64px;
    letter-spacing: 6px;
    color: var(--wordmark-muted);
  }

  .edge-band { position: absolute; }
  .edge-band--top { top: 0; left: 0; right: 0; height: 22px; background: var(--band-sky); }
  .edge-band--bottom { bottom: 0; left: 0; right: 0; height: 22px; background: var(--band-sky); }
  .edge-band--left { top: 0; bottom: 0; left: 0; width: 30px; background: var(--band-gold); }
  .edge-band--right { top: 0; bottom: 0; right: 0; width: 30px; background: var(--band-orange); }

  .holder { position: absolute; left: 78px; top: 62px; color: var(--text-light); }
  .holder__name { font-size: 21px; }
  .holder__title { font-size: 16px; margin-top: 8px; margin-left: -6px; }

  .address {
    position: absolute; left: 72px; top: 246px;
    color: var(--text-light); font-size: 16px; line-height: 28px;
  }
  .address__line--indent { padding-left: 20px; }

  .front-wordmark {
    position: absolute; right: 74px; top: 176px;
    font-family: "Montserrat", sans-serif;
    font-weight: 500; font-size: 34px; letter-spacing: 3px;
    color: var(--wordmark-muted);
  }

  .contacts {
    position: absolute; right: 74px; top: 236px;
    color: var(--text-light); font-size: 18px; line-height: 30px;
    list-style: none; text-align: left;
  }
</style>
</head>
<body>
  <section class="card card--back" aria-label="Card back">
    <div class="back-wordmark">VELMOTH</div>
  </section>

  <section class="card card--front" aria-label="Card front">
    <div class="edge-band edge-band--top" role="img" aria-label="Sky blue triangular edge pattern"></div>
    <div class="edge-band edge-band--bottom" role="img" aria-label="Sky blue triangular edge pattern"></div>
    <div class="edge-band edge-band--left" role="img" aria-label="Gold triangular edge pattern"></div>
    <div class="edge-band edge-band--right" role="img" aria-label="Orange triangular edge pattern"></div>

    <div class="holder">
      <p class="holder__name">Your Name</p>
      <p class="holder__title">Title</p>
    </div>

    <address class="address" style="font-style: normal;">
      <p class="address__line">A : Larkfield Road, Eastbrook</p>
      <p class="address__line address__line--indent">Morrow, New Jersey</p>
    </address>

    <div class="front-wordmark">VELMOTH</div>

    <ul class="contacts">
      <li>P : 012- 555- 0147</li>
      <li>E : yourname@velmoth.com</li>
      <li>W : www.velmoth.com</li>
    </ul>
  </section>
</body>
</html>
```